Varnell Skyworks Limited

Started a consulting business 12 months ago and have since moved location and have grown and seek to identify my self to the industry.
Specializing in quality solutions, business documentation and maintenance solution's

Industry/Entity Type

Business

```html
<!DOCTYPE html>
<html lang="en">
<head>
<meta charset="utf-8">
<title>Varnell Skyworks Limited – Business Cards</title>
<link rel="stylesheet" href="https://fonts.googleapis.com/css2?family=Questrial&family=Montserrat:wght@700&display=swap">
<style>
  :root {
    --navy: #283c5e;
    --navy-text: #1f2f52;
    --paper: #ffffff;
    --backdrop: #e9eaed;
  }
  * { box-sizing: border-box; margin: 0; padding: 0; }
  html, body { width: 1200px; height: 600px; overflow: hidden; }
  body { background: var(--backdrop); position: relative; font-family: "Questrial", sans-serif; }

  .card {
    position: absolute;
    top: 152px;
    width: 467px;
    height: 278px;
  }

  /* Reverse side */
  .card-back {
    left: 93px;
    background: var(--navy);
    display: flex;
    align-items: center;
    justify-content: center;
    gap: 12px;
  }
  .card-back .mark-square {
    width: 22px; height: 22px;
    border: 2px solid var(--paper);
  }
  .card-back .brand-name {
    color: var(--paper);
    font-size: 20px;
    letter-spacing: 0.5px;
  }

  /* Front side */
  .card-front {
    left: 638px;
    background: var(--paper);
    color: var(--navy-text);
  }
  .holder {
    position: absolute;
    left: 28px; top: 46px;
  }
  .holder-name {
    font-family: "Montserrat", sans-serif;
    font-weight: 700;
    font-size: 19px;
    line-height: 1;
  }
  .holder-role {
    font-size: 12px;
    margin-top: 2px;
  }

  .brand {
    position: absolute;
    left: 250px; top: 38px;
    display: flex;
    align-items: center;
    gap: 10px;
  }
  .brand .mark-square {
    width: 46px; height: 46px;
    background: var(--navy);
  }
  .brand .brand-name {
    font-size: 19px;
    line-height: 1.1;
    color: var(--navy-text);
  }

  .contact {
    position: absolute;
    left: 28px; top: 154px;
    font-size: 12px;
    line-height: 16px;
  }
  .contact strong { font-family: "Questrial", sans-serif; font-weight: 700; }
  .address { margin-top: 11px; line-height: 14.5px; }
</style>
</head>
<body>
  <section class="card card-back">
    <span class="mark-square"></span>
    <span class="brand-name">Varnell Skyworks Limited</span>
  </section>

  <section class="card card-front">
    <div class="holder">
      <p class="holder-name">Peter R Hale</p>
      <p class="holder-role">Manager / CEO</p>
    </div>

    <div class="brand">
      <span class="mark-square"></span>
      <span class="brand-name">Varnell Skyworks<br>Limited</span>
    </div>

    <div class="contact">
      <p>Mobile: +64 21 555 0148</p>
      <p>Email: <strong>varnellsky</strong>@mailhub.co.nz</p>
      <div class="address">
        <p>Unit B204, 18 Kestrel Road</p>
        <p>Harlow Park 2019</p>
        <p>Auckland NZ</p>
      </div>
    </div>
  </section>
</body>
</html>
```